Biz Cards for Lumivale Associates

Lumivale Associates is seeking a single-sided business card that is more visually-appealing than our current design (see attached).

Notes:
- Our colors are blue & teal.
- Our tag line must be large enough to be easily read
- We don't necessarily need our address included (that's just the biz office)
- We'd like to add our email address: Lumivale512@brindlemail.net

Thanks!

Industry/Entity Type

Business

Contact Information for Business Card

Standard size
PSD file required w/ text on its own layer

Colors
86cfc6
3277b5

```html
<!DOCTYPE html>
<html lang="en">
<head>
<meta charset="utf-8">
<title>Lumivale Associates – Business Card</title>
<link rel="stylesheet" href="https://fonts.googleapis.com/css2?family=Open+Sans:ital,wght@1,400&family=Roboto+Condensed:wght@400&family=Roboto:wght@400&display=swap">
<style>
  :root {
    --bg: #e4e5e6;
    --card: #ffffff;
    --ink: #1c1c1c;
    --ink-soft: #555555;
    --ink-muted: #6f6f6f;
    --band-grey: #6a6a6a;
    --band-grey-light: #8c8c8c;
    --teal: #86cfc6;
    --blue: #3277b5;
    --blue-light: #5a93c9;
  }
  html, body {
    margin: 0;
    width: 1200px;
    height: 1200px;
    overflow: hidden;
    background: var(--bg);
  }
  .canvas {
    width: 1200px;
    height: 1200px;
    display: flex;
    align-items: center;
    justify-content: center;
  }
  .business-card {
    position: relative;
    width: 1000px;
    height: 640px;
    background: var(--card);
    box-shadow: 0 2px 8px rgba(0,0,0,0.12);
    overflow: hidden;
  }
  .top-band {
    position: absolute;
    top: 0; left: 0; right: 0;
    height: 34px;
    background: linear-gradient(to bottom, var(--band-grey) 0 70%, var(--band-grey-light) 70% 100%);
  }
  .brand {
    position: absolute;
    top: 58px; left: 0; right: 0;
    text-align: center;
  }
  .brand-mark {
    display: block;
    margin: 0 auto;
  }
  .brand-name {
    margin: 22px 0 0;
    font-family: "Roboto Condensed", sans-serif;
    font-weight: 400;
    font-size: 66px;
    letter-spacing: 3px;
    line-height: 1;
    color: var(--ink);
  }
  .tagline {
    position: absolute;
    top: 334px; left: 0; right: 0;
    text-align: center;
    margin: 0;
    font-family: "Open Sans", sans-serif;
    font-style: italic;
    font-size: 21px;
    color: var(--blue);
    letter-spacing: -0.3px;
  }
  .website {
    position: absolute;
    top: 408px; left: 0; right: 0;
    text-align: center;
    margin: 0;
    font-family: "Roboto", sans-serif;
    font-size: 29px;
    letter-spacing: 1px;
    color: var(--ink);
  }
  .contact-line {
    position: absolute;
    top: 484px; left: 0; right: 0;
    text-align: center;
    margin: 0;
    font-family: "Roboto Condensed", sans-serif;
    font-size: 36px;
    color: var(--ink-soft);
  }
  .contact-line .email { color: #3a3a3a; }
  .address {
    position: absolute;
    top: 542px; left: 0; right: 0;
    text-align: center;
    margin: 0;
    font-family: "Roboto Condensed", sans-serif;
    font-size: 29px;
    color: var(--ink-muted);
  }
  .bottom-rule {
    position: absolute;
    left: 0; right: 0;
    bottom: 36px;
    height: 4px;
    background: var(--teal);
  }
  .bottom-band {
    position: absolute;
    left: 0; right: 0; bottom: 0;
    height: 32px;
    background: linear-gradient(to right, var(--blue-light), var(--blue));
  }
</style>
</head>
<body>
  <main class="canvas">
    <article class="business-card">
      <div class="top-band"></div>

      <header class="brand">
        <svg class="brand-mark" width="150" height="150" viewBox="0 0 150 150" aria-hidden="true">
          <circle cx="75" cy="75" r="72" fill="none" stroke="var(--ink)" stroke-width="3"/>
        </svg>
        <h1 class="brand-name">Lumivale Associates Ltd</h1>
      </header>

      <p class="tagline">Thoughtful Minds. Caring Hearts. Better Days.</p>
      <p class="website">Lumivale.net</p>
      <p class="contact-line">(855) LUMI-VAL • <span class="email">Lumivale512@brindlemail.net</span></p>
      <p class="address">4120 Alder Ridge Rd, Suite 310, Brookfield, OH&nbsp;&nbsp;44123</p>

      <div class="bottom-rule"></div>
      <div class="bottom-band"></div>
    </article>
  </main>
</body>
</html>
```